Manufacturing Company Business card

K & T is a leading supplier of complex machine parts, assemblies and sub assemblies to the aerospace industry.
we would like to create a new feel for our manufacturing company business card design.
We are into lean manufacturing, bold design, metal, use current logo, use "this is your life" logo for entire back of card. updated look for 2015, text, bardcode, etc

our primary end use is flight control components used on about all commercial and business jets in use as well as military aircraft and civil aviation.

Reason: Need more time to review with internal team at KTmfg:)

Target Market(s)

aerospace, manufacturing

Industry/Entity Type

Aero

Contact Information for Business Card

New, industrial, trendy, use current logo, we like text, vmail is lame :( cell ph is ok - what is a fax???

Font styles to use
Serif
Sans Serif

Requirements
Must have
• incorporate our current logo, one option is an Industrial look, metal etc. we can also try to incorporate the feel of the back of the card onto the front but not so busy.
• Back of card full size "this is your life"
• front side, barcode, cell, - our motto "solutions in manufacturing" tm
Nice to have
• Professional look
• up to date
• appeals to broad audience
Should not have
• too much content - pictures of planes

```html
<!DOCTYPE html>
<html lang="en">
<head>
<meta charset="utf-8">
<title>K &amp; T Manufacturing – Business Card</title>
<link rel="stylesheet" href="https://fonts.googleapis.com/css2?family=Arimo:wght@400;700&display=swap">
<style>
  :root {
    --page: #e9e7e2;
    --card: #f7f7f6;
    --card-edge: #e6e6e4;
    --ink: #1c1c1c;
    --ink-soft: #3a3a3a;
    --band-dark: #232323;
    --band-green: #19a874;
  }
  html, body {
    margin: 0;
    width: 1200px;
    height: 902px;
    overflow: hidden;
    background: var(--page);
    font-family: "Arimo", Arial, sans-serif;
  }
  .canvas { position: relative; width: 1200px; height: 902px; }
  .card {
    position: absolute;
    width: 700px;
    height: 400px;
    background: radial-gradient(ellipse at 40% 35%, #ffffff 0%, var(--card) 55%, var(--card-edge) 100%);
    box-shadow: 0 6px 18px rgba(0,0,0,.18);
    overflow: hidden;
  }
  .card--back { left: 60px; top: 48px; }
  .card--front { left: 440px; top: 454px; }
  .card__wave { position: absolute; inset: 0; width: 100%; height: 100%; z-index: 0; }
  .card > :not(.card__wave) { z-index: 1; }

  .brand {
    position: absolute;
    display: flex;
    align-items: center;
    gap: 12px;
    color: var(--ink-soft);
    font-weight: 700;
    font-size: 30px;
    line-height: 1;
    letter-spacing: .04em;
  }
  .brand__dot {
    width: 22px; height: 22px;
    border-radius: 50%;
    background: var(--band-green);
  }
  .card--back .brand { left: 150px; top: 76px; }
  .tagline {
    position: absolute;
    left: 150px; top: 140px;
    margin: 0;
    font-size: 58px;
    line-height: 1.15;
    font-weight: 400;
    color: var(--ink);
    letter-spacing: -.01em;
  }

  .card--front .brand { left: 70px; top: 48px; font-size: 26px; }
  .motto {
    position: absolute;
    left: 70px; top: 90px;
    margin: 0;
    font-size: 13px;
    line-height: 1;
    letter-spacing: .55em;
    color: var(--ink-soft);
  }
  .contact { position: absolute; left: 250px; top: 124px; color: var(--ink); line-height: 1.2; }
  .contact__name { margin: 0; font-size: 30px; font-weight: 700; }
  .contact__role { margin: 0 0 0 80px; font-size: 12px; color: var(--ink-soft); }
  .contact__phone { margin: 16px 0 0 110px; font-size: 17px; }
  .contact__address { margin: 6px 0 0 0; font-size: 17px; }
</style>
</head>
<body>
<main class="canvas">

  <section class="card card--back" aria-label="Back of card">
    <svg class="card__wave" viewBox="0 0 700 400" preserveAspectRatio="none" aria-hidden="true">
      <path fill="var(--band-green)" d="M0,364 C210,354 310,324 400,284 C480,250 570,238 700,236 L700,400 L0,400 Z"/>
      <path fill="#ffffff" d="M0,374 C212,365 314,336 404,296 C484,262 574,250 700,248 L700,400 L0,400 Z"/>
      <path fill="var(--band-dark)" d="M0,380 C214,372 318,343 408,303 C488,269 578,257 700,255 L700,400 L0,400 Z"/>
    </svg>
    <div class="brand"><span class="brand__dot"></span>K &amp; T Manufacturing</div>
    <h1 class="tagline">"this is your life"</h1>
  </section>

  <section class="card card--front" aria-label="Front of card">
    <svg class="card__wave" viewBox="0 0 700 400" preserveAspectRatio="none" aria-hidden="true">
      <path fill="var(--band-green)" d="M0,370 C230,362 340,344 430,314 C510,288 590,278 700,276 L700,400 L0,400 Z"/>
      <path fill="#ffffff" d="M0,379 C232,372 343,355 433,325 C513,299 593,289 700,287 L700,400 L0,400 Z"/>
      <path fill="var(--band-dark)" d="M0,385 C234,378 346,362 436,332 C516,306 596,296 700,294 L700,400 L0,400 Z"/>
    </svg>
    <div class="brand"><span class="brand__dot"></span>K &amp; T Manufacturing</div>
    <p class="motto">"solutions in manufacturing"</p>
    <div class="contact">
      <p class="contact__name">Employee name</p>
      <p class="contact__role">Managing Director</p>
      <p class="contact__phone">036-555 0142</p>
      <p class="contact__address">Your Address Inc 4th Mill Rd Harlow,OH 00000</p>
    </div>
  </section>

</main>
</body>
</html>
```